Coralbend Pastoral Traders Business Cards

We require business cards revamped with our logo. A few details we would like to use.

1. Round Edges
2. Our logo over the top of a wagyu cattle background photo on one side of the card

Other side of the card has the below details.

1. Person Name (First & Last)
2. Job Position
3. Mobile Number
4. Email Address
5. Website Address

Simple & Neat.

Target Market(s)

Sales

Industry/Entity Type

Agriculture

Contact Information for Business Card

CORALBEND PASTORAL TRADERS

Colors

Designer to choose colors to be used in the design.

Requirements
Must have
• Company Logo

```html
<!DOCTYPE html>
<html lang="en">
<head>
<meta charset="utf-8">
<title>Coralbend Pastoral Traders – Business Cards</title>
<link rel="stylesheet" href="https://fonts.googleapis.com/css2?family=Roboto:wght@400;700&display=swap">
<style>
  :root {
    --page: #e6d3ae;
    --cream-top: #efe3c8;
    --cream-mid: #f8f3ea;
    --maroon: #7a2437;
    --white: #ffffff;
    --green-light: #b9d08c;
    --green-deep: #7fa255;
  }
  * { box-sizing: border-box; margin: 0; padding: 0; }
  html, body { width: 1200px; height: 853px; overflow: hidden; }
  body {
    background: var(--page);
    font-family: "Roboto", sans-serif;
    display: flex;
    align-items: center;
    justify-content: center;
    gap: 40px;
  }
  .card {
    position: relative;
    width: 540px;
    height: 309px;
    border-radius: 22px;
    overflow: hidden;
    background: linear-gradient(180deg, var(--cream-top) 0%, var(--cream-mid) 45%, var(--cream-mid) 100%);
    box-shadow: 0 6px 18px rgba(90, 60, 20, 0.18);
  }
  .card-art { position: absolute; inset: 0; width: 100%; height: 100%; }
  .brand {
    position: absolute;
    display: flex;
    align-items: center;
    gap: 12px;
    color: var(--maroon);
    font-weight: 700;
  }
  .brand-mark {
    width: 34px; height: 34px;
    border-radius: 50%;
    background: var(--maroon);
    flex: none;
  }
  .brand-name { font-size: 25px; line-height: 1.1; letter-spacing: 0.5px; }
  .front .brand { left: 230px; top: 36px; }
  .back .brand { left: 250px; top: 58px; }
  .contact-person {
    position: absolute;
    left: 26px; top: 150px;
    color: var(--white);
  }
  .person-name { font-size: 15px; font-weight: 700; }
  .person-role { font-size: 12px; margin-top: 2px; }
  .contact-list {
    list-style: none;
    position: absolute;
    color: var(--white);
    font-size: 13px;
  }
  .contact-list li { display: flex; align-items: center; gap: 7px; margin-bottom: 6px; }
  .contact-list.primary { left: 26px; top: 200px; }
  .contact-list.secondary { right: 24px; top: 248px; text-align: right; }
  .contact-list.secondary li { justify-content: flex-end; }
  .icon {
    width: 14px; height: 14px;
    background: var(--white);
    border-radius: 3px;
    display: inline-flex; align-items: center; justify-content: center;
    flex: none;
  }
  .icon svg { width: 10px; height: 10px; }
</style>
</head>
<body>

  <section class="card front" aria-label="Business card, contact side">
    <svg class="card-art" viewBox="0 0 540 309" aria-hidden="true">
      <path d="M0,138 C140,122 260,160 360,200 C430,226 490,226 540,204 L540,309 L0,309 Z" fill="var(--maroon)"/>
    </svg>
    <div class="brand">
      <span class="brand-mark"></span>
      <span class="brand-name">Coralbend<br>Pastoral Traders</span>
    </div>
    <div class="contact-person">
      <p class="person-name">Person Name</p>
      <p class="person-role">Job Position</p>
    </div>
    <ul class="contact-list primary">
      <li><span class="icon"><svg viewBox="0 0 10 10"><rect x="2.5" y="0.5" width="5" height="9" rx="1" fill="none" stroke="var(--maroon)" stroke-width="1.2"/></svg></span>+0 123 456 789</li>
      <li><span class="icon"><svg viewBox="0 0 10 10"><rect x="0.5" y="2" width="9" height="6" fill="none" stroke="var(--maroon)" stroke-width="1.1"/><path d="M0.5,2 L5,5.5 L9.5,2" fill="none" stroke="var(--maroon)" stroke-width="1.1"/></svg></span>email@coralbend.com</li>
    </ul>
    <ul class="contact-list secondary">
      <li>Website Address<span class="icon"><svg viewBox="0 0 10 10"><circle cx="5" cy="5" r="4" fill="none" stroke="var(--maroon)" stroke-width="1.1"/><path d="M1,5 H9 M5,1 C3,3.5 3,6.5 5,9 M5,1 C7,3.5 7,6.5 5,9" fill="none" stroke="var(--maroon)" stroke-width="0.9"/></svg></span></li>
      <li>location<span class="icon"><svg viewBox="0 0 10 10"><path d="M5,9.5 C2,6 1.8,4.6 1.8,3.7 A3.2,3.2 0 0 1 8.2,3.7 C8.2,4.6 8,6 5,9.5 Z" fill="var(--maroon)"/><circle cx="5" cy="3.8" r="1.2" fill="var(--white)"/></svg></span></li>
    </ul>
  </section>

  <section class="card back" aria-label="Business card, brand side">
    <svg class="card-art" viewBox="0 0 540 309">
      <defs>
        <linearGradient id="pasture" x1="0" y1="0" x2="0" y2="1">
          <stop offset="0" stop-color="var(--green-light)"/>
          <stop offset="1" stop-color="var(--green-deep)"/>
        </linearGradient>
      </defs>
      <path role="img" aria-label="Illustration of wagyu cattle grazing on green hills beside farm buildings"
            d="M0,120 C80,95 170,110 240,160 C300,205 350,250 420,270 C470,285 510,290 540,290 L540,309 L0,309 Z"
            fill="url(#pasture)"/>
    </svg>
    <div class="brand">
      <span class="brand-mark"></span>
      <span class="brand-name">Coralbend<br>Pastoral Traders</span>
    </div>
  </section>

</body>
</html>
```